Rising Stewards Scheme. Brochure to Inform Target Audience.

Rising Steward Scheme:

4 Page Brochure
Aimed at Parents and Children (Age 11-16)
Programme Overview
Specific Focus on Copperleaf Award with Learning Objectives and Enabling Objectives from Content Document
Contact Area Needed
How to Book - Online through the Website
Should encourage people to want to join it or sign up

you can use stock rugby images if needed

Target Market(s)

children between ages 11-16 and parents, gatekeepers (schools, rugby clubs)

Industry/Entity Type

Education

Font styles to use
Serif
Sans Serif

Requirements
Must have
• the programme content, each award continent and Copperleaf Award learning objectives
• Colours should match existing work that has been created
• Get in touch: www.harvestmark-rss.com
• maren@harvestmark-rss.com
Nice to have
• graphics of kids playing rugby if possible from stock images

```html
<!DOCTYPE html>
<html lang="en">
<head>
<meta charset="utf-8">
<title>Rising Stewards Scheme – Brochure Spread</title>
<link rel="stylesheet" href="https://fonts.googleapis.com/css2?family=Montserrat:wght@300;400;600;700;800;900&family=Open+Sans:wght@400;600&family=Oswald:wght@500;600&display=swap">
<style>
  :root {
    --ink: #141414;
    --ink-soft: #1f1f1f;
    --yellow: #f7c21a;
    --yellow-deep: #e5a90b;
    --white: #ffffff;
    --body-grey: #b9b9b9;
    --backdrop: #e4e4e4;
  }
  * { margin: 0; padding: 0; box-sizing: border-box; }
  html, body { width: 1200px; height: 824px; overflow: hidden; background: var(--backdrop); }
  .spread { position: relative; width: 1200px; height: 824px; display: flex; }
  .page {
    position: relative; width: 600px; height: 824px; overflow: hidden;
    background: linear-gradient(160deg, var(--ink-soft), var(--ink) 60%);
    font-family: "Open Sans", sans-serif; color: var(--white);
  }
  .page--back { border-right: 1px solid #000; }
  .layer { position: absolute; left: 0; top: 0; }

  /* Back page */
  .overview { position: absolute; left: 60px; top: 96px; width: 480px; }
  .overview__title { font-family: "Montserrat", sans-serif; font-weight: 400; font-size: 22px; letter-spacing: .5px; }
  .overview__title strong { color: var(--yellow); font-weight: 800; }
  .rule { display: block; width: 34px; height: 4px; border-radius: 2px; background: var(--yellow); margin: 10px 0 14px; }
  .overview__text { font-size: 11.5px; line-height: 1.55; color: var(--body-grey); text-align: justify; }

  .medal {
    position: absolute; border-radius: 50%;
    display: flex; align-items: center; justify-content: center; text-align: center;
    font-family: "Montserrat", sans-serif; font-weight: 900; line-height: 1.05;
    color: #2b2b2b; box-shadow: 0 6px 14px rgba(0,0,0,.5);
  }
  .medal--silver { left: 140px; top: 584px; width: 116px; height: 116px; font-size: 14px;
    background: radial-gradient(circle at 35% 30%, #ffffff, #c9c9c9 45%, #8d8d8d 100%); border: 5px solid #a9a9a9; }
  .medal--gold { left: 252px; top: 530px; width: 136px; height: 136px; font-size: 16px;
    background: radial-gradient(circle at 35% 30%, #fff3a0, #f2c21a 45%, #b98606 100%); border: 6px solid #d7a40c; }
  .medal--copper { left: 390px; top: 500px; width: 112px; height: 112px; font-size: 13px; color: #3a1c08;
    background: radial-gradient(circle at 35% 30%, #f2b07a, #cf7a3a 45%, #8c4418 100%); border: 5px solid #b0602a; }

  .contact { position: absolute; left: 300px; top: 688px; }
  .contact__title { font-family: "Montserrat", sans-serif; font-weight: 800; font-size: 17px; color: var(--yellow); letter-spacing: .5px; }
  .contact__line { display: flex; align-items: center; gap: 8px; font-size: 13px; margin-top: 6px; }
  .contact__line .icon { width: 12px; height: 12px; }
  .contact__line b { font-weight: 600; }

  /* Front page */
  .headline { position: absolute; left: 66px; top: 70px; font-family: "Montserrat", sans-serif; }
  .headline__lead { display: block; font-weight: 300; font-size: 30px; letter-spacing: 1px; }
  .headline__accent { display: block; font-weight: 900; font-size: 42px; color: var(--yellow); line-height: 1; }
  .headline__tail { display: block; font-weight: 700; font-size: 23px; letter-spacing: 1px; margin-top: 4px; }
  .headline .rule { width: 36px; margin-top: 10px; }

  .brand { position: absolute; left: 392px; top: 36px; width: 180px; text-align: center; }
  .brand__mark { display: flex; align-items: center; justify-content: center; gap: 8px;
    font-family: "Montserrat", sans-serif; font-weight: 800; font-size: 15px; color: var(--yellow); letter-spacing: .5px; }
  .brand__dot { width: 16px; height: 16px; border-radius: 50%; background: var(--yellow); }
  .scheme { margin-top: 46px; font-family: "Oswald", sans-serif; color: var(--yellow); }
  .scheme__name { display: block; font-weight: 600; font-size: 27px; line-height: 1; letter-spacing: .5px; }
  .scheme__sub { display: flex; align-items: center; gap: 6px; justify-content: center; font-size: 10px; letter-spacing: 3px; margin-top: 3px; }
  .scheme__sub::before, .scheme__sub::after { content: ""; flex: 1; height: 1px; background: var(--yellow); }

  .cover-web { position: absolute; left: 300px; top: 770px; display: flex; gap: 8px; align-items: center; font-size: 13px; }
  .cover-web .icon { width: 12px; height: 12px; }
  .cover-web b { font-weight: 600; }
</style>
</head>
<body>
<main class="spread">

  <!-- Back page -->
  <section class="page page--back">
    <svg class="layer" width="600" height="824" viewBox="0 0 600 824" role="img" aria-label="Action photo of a rugby team performing a pre-match challenge on a floodlit pitch">
      <defs>
        <linearGradient id="teamPhoto" x1="0" y1="0" x2="0" y2="1">
          <stop offset="0" stop-color="#2a2a2a"/>
          <stop offset=".6" stop-color="#333a30"/>
          <stop offset="1" stop-color="#3f5a2e"/>
        </linearGradient>
      </defs>
      <path d="M0 300 C160 285 420 300 600 265 L600 560 C430 610 240 660 0 720 Z" fill="url(#teamPhoto)"/>
    </svg>
    <svg class="layer" width="600" height="824" viewBox="0 0 600 824" aria-hidden="true">
      <path d="M0 824 L0 760 C160 690 360 650 600 560 L600 824 Z" fill="#121212"/>
      <path d="M0 760 C160 690 360 650 600 560 L600 578 C370 665 170 712 0 790 Z" fill="var(--yellow)"/>
    </svg>

    <div class="overview">
      <h2 class="overview__title">PROGRAMME <strong>OVERVIEW</strong></h2>
      <span class="rule"></span>
      <p class="overview__text">The Harvestmark team have created a programme which enables each individual to maximise their learning potential so that you can be the best you can be. We provide a fun and healthy environment which is supported by highly motivated coaches which provide excellent individual care and attention. The programme is delivered over three Awards: Copperleaf, Silver and Gold.</p>
    </div>

    <div class="medal medal--silver">SILVER<br>AWARD</div>
    <div class="medal medal--gold">GOLD<br>AWARD</div>
    <div class="medal medal--copper">COPPERLEAF<br>AWARD</div>

    <div class="contact">
      <h3 class="contact__title">GET IN TOUCH</h3>
      <span class="rule" style="margin:6px 0 4px;width:22px;height:3px"></span>
      <p class="contact__line">
        <svg class="icon" viewBox="0 0 12 12" aria-hidden="true"><rect x="0.5" y="2" width="11" height="8" fill="none" stroke="var(--yellow)"/><path d="M0.5 2 L6 7 L11.5 2" fill="none" stroke="var(--yellow)"/></svg>
        maren@harvestmark-rss.com
      </p>
      <p class="contact__line">
        <svg class="icon" viewBox="0 0 12 12" aria-hidden="true"><circle cx="6" cy="6" r="5.3" fill="none" stroke="var(--yellow)"/><path d="M0.7 6 H11.3 M6 0.7 C3 4 3 8 6 11.3 C9 8 9 4 6 0.7" fill="none" stroke="var(--yellow)"/></svg>
        <span>www.<b>harvestmark-rss</b>.com</span>
      </p>
    </div>
  </section>

  <!-- Front page -->
  <section class="page page--front">
    <svg class="layer" width="600" height="824" viewBox="0 0 600 824" role="img" aria-label="Photo of a rugby player running with the ball in front of a stadium crowd">
      <defs>
        <linearGradient id="playerPhoto" x1="0" y1="0" x2="1" y2="1">
          <stop offset="0" stop-color="#3b5e3c"/>
          <stop offset=".5" stop-color="#2f6b4c"/>
          <stop offset="1" stop-color="#5f7f3a"/>
        </linearGradient>
      </defs>
      <path d="M60 470 C140 350 420 360 600 230 L600 620 C440 640 300 690 170 740 C110 660 60 560 60 470 Z" fill="url(#playerPhoto)"/>
    </svg>
    <svg class="layer" width="600" height="824" viewBox="0 0 600 824" aria-hidden="true">
      <path d="M40 490 C120 370 390 380 600 225" fill="none" stroke="var(--yellow)" stroke-width="2"/>
      <path d="M60 480 C80 430 150 410 220 395 C140 430 100 470 80 540 Z" fill="var(--yellow)"/>
      <path d="M170 740 C300 690 440 640 600 620 L600 650 C450 665 300 710 175 760 Z" fill="var(--yellow)"/>
      <path d="M175 760 C300 712 450 668 600 650 L600 824 L150 824 Z" fill="#121212"/>
      <path d="M200 760 C320 720 470 690 600 685" fill="none" stroke="var(--white)" stroke-width="1"/>
    </svg>

    <h1 class="headline">
      <span class="headline__lead">INSPIRING</span>
      <span class="headline__accent">THE NEXT</span>
      <span class="headline__tail">GENERATION</span>
      <span class="rule"></span>
    </h1>

    <div class="brand">
      <div class="brand__mark"><span class="brand__dot"></span>HARVESTMARK STEWARDS</div>
      <div class="scheme">
        <span class="scheme__name">RISING STEWARDS</span>
        <span class="scheme__sub">SCHEME</span>
      </div>
    </div>

    <p class="cover-web">
      <svg class="icon" viewBox="0 0 12 12" aria-hidden="true"><circle cx="6" cy="6" r="5.3" fill="none" stroke="var(--yellow)"/><path d="M0.7 6 H11.3 M6 0.7 C3 4 3 8 6 11.3 C9 8 9 4 6 0.7" fill="none" stroke="var(--yellow)"/></svg>
      <span>www.<b>harvestmark-rss</b>.com</span>
    </p>
  </section>

</main>
</body>
</html>
```